Small IT consulting firm needs a new web site

Quellmark Systems, LLC is a company based out of Arizona with national presence. We work on both national, multinational, and international projects. We are Brantova Partners. Heavy experience and work with Nodewell Control Suite, Velquo, Trellin 820 . We offer Architecture, Design, Development, and implementation services. We have a specialty in Trellin 820 migrations and implementations. We also have a specialized practice in Program and Project Management. The design message should foster a feeling of partnership and experience. Attached is my logo.
Industry/Entity Type
It Company
Coding
Coded - Design and coding required
Number of Pages Required
5+ page
Look and feel

```html
<!DOCTYPE html>
<html lang="en">
<head>
<meta charset="utf-8">
<title>Quellmark Systems, LLC</title>
<link rel="stylesheet" href="https://fonts.googleapis.com/css2?family=Open+Sans:wght@400;600&family=Arimo:wght@400;700&family=Orbitron:wght@700&display=swap">
<style>
:root{
  --red:#d42a2f;
  --red-dark:#b81f24;
  --ink:#222;
  --text:#333;
  --muted:#666;
  --page:#f4f4f4;
  --card:#ffffff;
  --line:#e2e2e2;
  --btn:#6b6b6b;
  --footer:#666666;
  --footer-text:#e4e4e4;
  --bottom:#4a4a4a;
  --sky-top:#8fb2d8;
  --sky-low:#dfe9f4;
}
*{box-sizing:border-box;margin:0;padding:0}
html,body{width:919px;height:1200px;overflow:hidden}
body{position:relative;background:var(--page);font-family:"Arimo",Arial,sans-serif;color:var(--text)}
.abs{position:absolute}

.site-header{left:0;top:0;width:919px;height:95px;background:linear-gradient(180deg,#bcd0e6 0%,#e9eff6 100%);border-bottom:2px solid var(--red)}
.brand{left:110px;top:22px;display:flex;align-items:center;gap:10px}
.brand-mark{width:34px;height:34px;background:var(--red)}
.brand-name{font-family:"Open Sans",sans-serif;font-weight:600;font-size:21px;color:var(--red);line-height:1}
.brand-tag{font-family:"Open Sans",sans-serif;font-size:8px;color:#555;letter-spacing:.5px;margin-top:4px}
.phone{left:694px;top:15px;display:flex;align-items:center;gap:5px;color:var(--red);font-size:16px}
.main-nav{left:584px;top:73px;display:flex;gap:31px;font-size:13px;color:#333}

.hero{left:0;top:97px;width:919px;height:301px;background:linear-gradient(180deg,var(--sky-top) 0%,var(--sky-low) 55%,#6f6a62 80%,#3d3a36 100%);border-bottom:3px solid var(--red)}
.hero-title{font-family:"Orbitron",sans-serif;font-weight:700;color:var(--red);font-size:24px;letter-spacing:1px}
.hero-line1{left:392px;top:30px}
.hero-line2{left:478px;top:72px}
.slider-dots{left:430px;top:273px;display:flex;gap:4px}
.slider-dots span{width:12px;height:12px;background:#fff;border:1px solid #ccc}
.slider-dots span.active{background:var(--red-dark)}

.service{width:227px;height:153px;top:453px;background:var(--card);border:1px solid var(--line);text-align:center}
.service-icon{position:absolute;left:78px;top:-35px;width:70px;height:70px;border-radius:50%;background:var(--red)}
.service h3{font-family:"Open Sans",sans-serif;font-weight:400;font-size:12.5px;color:#444;margin:43px 13px 0;text-align:left;line-height:1.1;white-space:nowrap}
.service p{font-size:9px;color:#555;line-height:1.45;margin:8px 14px 0;text-align:left}
.service .learn{position:absolute;left:62px;top:118px;width:102px;height:25px;background:var(--btn);color:#fff;font-family:"Open Sans",sans-serif;font-style:italic;font-size:10px;line-height:25px;border-bottom:2px solid #333;border-radius:2px}
.s1{left:104px}.s2{left:346px}.s3{left:588px}
.s2 h3{margin-top:43px;white-space:normal}
.s2 p{margin-top:4px}

.welcome{left:104px;top:672px;width:492px}
.welcome h1{font-family:"Open Sans",sans-serif;font-weight:400;font-size:19px;color:var(--ink)}
.welcome h1 em{font-style:normal;color:var(--red)}
.welcome p{font-size:10.5px;line-height:1.6;margin:0 0 16px 2px;color:#333}
.welcome .lead{margin-top:12px}
.welcome .lead em{font-style:normal;color:var(--red)}

.request{left:636px;top:660px;width:179px}
.request h2{font-family:"Open Sans",sans-serif;font-weight:400;font-size:15.5px;color:#333;margin-bottom:9px}
.field{display:block;height:21px;background:#fff;border:1px solid #e6e6e6;font-size:8px;font-style:italic;color:#888;padding:6px 8px;margin-bottom:5px}
.field.area{height:66px}
.send{height:27px;background:#8a8a8a;border-bottom:2px solid #555;color:#fff;font-size:15px;text-align:center;line-height:26px;margin-top:-1px}

.clients-note{left:107px;top:888px;font-size:9.5px;color:#222}
.clients{left:105px;top:914px;width:709px;height:95px;background:#dedede;border:2px solid #c9c9c9;padding:12px 10px;display:flex;gap:4px}
.client{flex:1;background:#fff;border:1px solid #cfcfcf;display:flex;align-items:center;justify-content:center;font-family:"Open Sans",sans-serif;font-weight:600;font-size:12px;color:#555;text-align:center}

.site-footer{left:0;top:1025px;width:919px;height:150px;background:var(--footer);color:var(--footer-text)}
.foot-col{position:absolute;top:10px}
.foot-col h4{font-family:"Open Sans",sans-serif;font-weight:400;font-size:14px;line-height:18px;color:#fff;padding-bottom:2px;border-bottom:1px dashed #999;width:111px;margin-bottom:5px}
.foot-col p,.foot-col li{font-family:"Open Sans",sans-serif;font-size:10px;line-height:13px;list-style:none}
.menu li{margin-bottom:9px}
.hours{border-collapse:collapse}
.hours td{font-family:"Open Sans",sans-serif;font-size:10px;line-height:12.5px;height:12.5px;padding:0;white-space:nowrap}
.hours td+td{padding-left:14px}
.hours .gap td{padding-top:12px}
.divider{position:absolute;top:45px;width:1px;height:72px;background:#7b7b7b}
.copyright{left:0;top:1175px;width:919px;height:25px;background:var(--bottom);color:#ccc;font-family:"Open Sans",sans-serif;font-size:7.5px;text-align:center;line-height:25px}
</style>
</head>
<body>

<header class="site-header abs">
  <div class="brand abs">
    <div class="brand-mark"></div>
    <div>
      <div class="brand-name">Quellmark Systems, LLC</div>
      <div class="brand-tag">WELCOME TO THE CYBER-AGE.</div>
    </div>
  </div>
  <div class="phone abs">
    <svg width="16" height="16" viewBox="0 0 24 24" aria-hidden="true"><path fill="#333" d="M6.6 10.8a15 15 0 0 0 6.6 6.6l2.2-2.2c.3-.3.7-.4 1-.2 1.1.4 2.3.6 3.6.6.6 0 1 .4 1 1V20c0 .6-.4 1-1 1A17 17 0 0 1 3 4c0-.6.4-1 1-1h3.5c.6 0 1 .4 1 1 0 1.3.2 2.5.6 3.6.1.3 0 .7-.2 1z"/></svg>
    <span>388-555-0172</span>
  </div>
  <nav class="main-nav abs"><span>HOME</span><span>SERVICES</span><span>CONTACT US</span></nav>
</header>

<section class="hero abs" role="img" aria-label="Photo of two climbers on a rocky mountain ridge, one helping the other up, against a blue sky">
  <div class="hero-title hero-line1 abs">WE'RE COMMITTED</div>
  <div class="hero-title hero-line2 abs">TO YOUR SUCCESS</div>
  <div class="slider-dots abs"><span class="active"></span><span></span><span></span><span></span></div>
</section>

<article class="service s1 abs">
  <div class="service-icon" role="img" aria-label="Office chair icon"></div>
  <h3>Program and Project Management</h3>
  <p>Experienced management for your initiatives. We have Certified and non-Certified PM's to fit your every initiative.</p>
  <div class="learn">Learn more</div>
</article>
<article class="service s2 abs">
  <div class="service-icon" role="img" aria-label="Pencil cup icon"></div>
  <h3>Technical Architecture, Design &amp; Engineering</h3>
  <p>Let us lead you in to the Cyber-Age by taking a seat at your table and helping you to employ the proper technologies for your succesful business..</p>
  <div class="learn">Learn more</div>
</article>
<article class="service s3 abs">
  <div class="service-icon" role="img" aria-label="Team of people icon"></div>
  <h3 style="text-align:center">Staff Augmentation</h3>
  <p>We can help with your temporary or long term consultant needs. Form Service Desk, Desktop Support, Networking, ETL DBA's or anything in between, give us a call, can help..</p>
  <div class="learn">Learn more</div>
</article>

<section class="welcome abs">
  <h1>Welcome to <em>Quellmark Systems, LLC</em></h1>
  <p class="lead">If you're looking &nbsp;for high quality and personal service, you've come to the ritht place. At <em>Quellmark Systems, LLC</em>, we'll give you the attention and personal service you'll come to expect and enjoy.</p>
  <p>Our staff has more then 24 year's of direct hands on experience in the Information Technology industry.</p>
  <p>We have worked with Fortune 500 companies as well as companies with a much smaller presence.</p>
</section>

<aside class="request abs">
  <h2>Request Information</h2>
  <div class="field">Name..</div>
  <div class="field">Email address..</div>
  <div class="field">Tel no..</div>
  <div class="field area">Request info.</div>
  <div class="send">Send</div>
</aside>

<p class="clients-note abs">HERE IS JUST A SAMPLING OF THE CLIENTS (*) THAT OUR STAF HAS WORKED WITH OVER THE YEARS.</p>
<section class="clients abs">
  <div class="client">Ridgeline Bank</div>
  <div class="client">Kanrei Motors</div>
  <div class="client">Carrowby Health</div>
  <div class="client">Tessman Controls</div>
  <div class="client">Coastal Fleet Service</div>
</section>

<footer class="site-footer abs">
  <div class="foot-col menu" style="left:104px">
    <h4>Site Menu</h4>
    <ul><li>Home</li><li>Services</li><li>Contact us</li></ul>
  </div>
  <div class="divider" style="left:259px"></div>
  <div class="foot-col" style="left:356px">
    <h4>Contact Info</h4>
    <p>1180 W Canyon Ridge Road Suite 204<br>Tempe, AZ 85281</p>
    <p style="margin-top:12px">388-555-0172</p>
  </div>
  <div class="divider" style="left:597px"></div>
  <div class="foot-col" style="left:696px">
    <h4>Hours</h4>
    <table class="hours">
      <tr><td>Monday</td><td>3 AM - 6 PM</td></tr>
      <tr><td>Tuesday</td><td>3 AM - 6 PM</td></tr>
      <tr><td>Wednesday</td><td>3 AM - 6 PM</td></tr>
      <tr><td>Thursday</td><td>3 AM - 6 PM</td></tr>
      <tr><td>Friday</td><td>3 AM - 6 PM</td></tr>
      <tr class="gap"><td>Saturday</td><td>Closed</td></tr>
      <tr><td>Sunday</td><td>Closed</td></tr>
    </table>
  </div>
</footer>
<div class="copyright abs">Copyright © 2015 Quellmark Systems, LLC, All rights reserved.</div>

</body>
</html>
```